"Velvet Crest" sexual performance enhancement pill bottle label needed.

This should be interesting...

I am starting a line of sexual performance enhancement products. This will be the first of several products basically. Keep in mind, I am the type of business person to stay with one company for years if they provide me with quality work.

This particular product is a male sexual performance pill. The name of the product is "Velvet Crest." The packaging of the pills are a black bottle with a white top. Label on the product example would be perfect but at a minimum I have attached a "template" for your guidance.

Some of the technical aspects of this are as follows:

-File Format: Illustrator CS6 is preferred. (Winner must provide artwork in layer and can not flatten artwork.)
-Resolution: 300 dpi minimum
-Bleed: 1/16th (0.0625") inch from edge of label
-Color Mode: CMYK only or must be converted to CMYK for final production

Lastly, this is your project as a designer, artist, creator, this is essentially a piece of you that will be sold and known by thousands of people. I have no color scheme that I prefer, just use the template and follow the layout. If you have any further questions, please feel free to contact me at any time.
Updates

Quick note on the product and what it does: -Powerful, long lasting, harder erections -Works in a minutes and last for hours -Enhances sexual desire and drive Thank you for your ideas...

Project Deadline Extended
Reason: We decided to extent the project for a few more days to let the last few concepts come in. So far things are looking really good and we definitely have seen some amazing designs. Thank you for your hard work and amazing creativity. Looking forward to seeing what we have come in the next couple of day. Very respectfully, Brock

ONLY THREE DAYS LEFT!!!! Please submit your ideas as soon as possible. And as always, thank you for your help!!! V/r, Brock

Industry/Entity Type

Graphic Design

```html
<!DOCTYPE html>
<html lang="en">
<head>
<meta charset="utf-8">
<title>Velvet Crest – Bottle Label</title>
<link href="https://fonts.googleapis.com/css2?family=Montserrat:wght@700;800&family=Open+Sans:wght@400;600;700;800&family=PT+Serif:wght@400;700&display=swap" rel="stylesheet">
<style>
  :root{
    --ink:#1d1d20;
    --ink-soft:#2a2a2e;
    --blue:#1e9ad6;
    --white:#ffffff;
    --copy:#e6e6e6;
    --rule:#4a4a4f;
    --page:#ffffff;
    --emblem-top:#e9e9ec;
    --emblem-bottom:#a9a9ae;
  }
  *{box-sizing:border-box;margin:0;padding:0}
  html,body{width:1200px;height:555px;overflow:hidden;background:var(--page)}
  .canvas{position:relative;width:1200px;height:555px}

  .label{position:absolute;left:442px;top:42px;width:738px;height:316px;background:var(--ink);color:var(--white);font-family:"Open Sans",Arial,sans-serif;overflow:hidden}

  .band{position:absolute;left:0;top:226px;width:100%;height:60px;background:var(--blue)}
  .footer{position:absolute;left:0;top:286px;width:100%;height:30px;background:var(--ink)}
  .divider{position:absolute;top:0;width:1px;height:100%;background:var(--rule)}
  .divider--a{left:228px}
  .divider--b{left:504px}

  /* left panel */
  .claims{position:absolute;left:8px;top:12px;width:214px;font-family:"Open Sans",Arial,sans-serif;font-weight:800;font-size:16px;line-height:19.5px;text-align:center;letter-spacing:-.2px}
  .copy{position:absolute;left:14px;width:204px;font-family:"PT Serif",Georgia,serif;font-size:7.2px;line-height:8.8px;text-align:justify;color:var(--copy)}
  .copy--one{top:140px}
  .copy--two{top:200px}
  .maker{position:absolute;left:12px;top:232px;width:206px;font-size:9px;line-height:11px}
  .maker strong{font-weight:800;display:block}

  /* centre panel */
  .brand{position:absolute;left:228px;top:36px;width:276px;text-align:center;font-family:"Montserrat",Arial,sans-serif;font-weight:800;font-size:34px;line-height:38px;color:var(--blue);letter-spacing:.5px}
  .emblem{position:absolute;left:316px;top:100px;width:100px;height:160px;border-radius:4px;background:linear-gradient(180deg,var(--emblem-top) 0%,var(--emblem-bottom) 100%)}
  .count{position:absolute;left:441px;top:234px;width:60px;text-align:center;font-family:"Montserrat",Arial,sans-serif;font-weight:800;font-size:28px;line-height:29px}
  .count small{display:block;font-family:"PT Serif",Georgia,serif;font-weight:400;font-size:11px;line-height:12px;letter-spacing:1px}
  .tagline{position:absolute;left:274px;top:290px;width:180px;height:22px;background:var(--ink-soft);border-bottom:1px solid #777;text-align:center;font-family:"PT Serif",Georgia,serif;font-size:13px;line-height:22px;color:#f0f0f0}

  /* right panel */
  .facts{position:absolute;left:530px;top:14px;width:196px;height:206px;background:var(--white);color:#111;padding:6px 8px;font-size:7px;line-height:9px}
  .facts h2{font-family:"Open Sans",Arial,sans-serif;font-weight:800;font-size:15px;line-height:17px}
  .facts .rule-thick{height:4px;background:#111;margin:2px 0}
  .facts .rule-thin{height:1px;background:#111;margin:2px 0}
  .facts .row{display:flex;justify-content:space-between;font-weight:700}
  .facts p{text-align:justify}
  .info{position:absolute;left:514px;top:232px;width:216px;font-size:9px;line-height:11px}
  .info strong{font-weight:800}

  .web{position:absolute;top:295px;font-family:"Open Sans",Arial,sans-serif;font-weight:800;font-size:10.5px;letter-spacing:.3px}
  .web--left{left:30px}
  .web--right{left:532px}
</style>
</head>
<body>
<main class="canvas">
  <section class="label" aria-label="Velvet Crest bottle label">
    <div class="band"></div>
    <div class="footer"></div>
    <div class="divider divider--a"></div>
    <div class="divider divider--b"></div>

    <h1 class="claims">Powerful, long lasting,<br>harder erections<br>Works in a minutes and<br>last for hours<br>Enhances sexual desire<br>and drive</h1>
    <p class="copy copy--one">Morbi gravida massa at est condimentum, in vestibulum velit mattis. Aenean auctor luctus accumsan. Quisque vestibulum porta erat ut auctor. Suspendisse varius condimentum commodo. Sed lacus libero, placerat sed interdum fringilla, gravida at sapien. Sed eu ipsum a tortor dapibus posuere. Quisque eu pretium sapien.</p>
    <p class="copy copy--two">Cras id nunc mi. Proin scelerisque est scelerisque rutrum venenatis. Praesent eget vestibulum nisl. Ut nunc augue,</p>
    <p class="maker"><strong>Manufactured by:</strong>Lorem ipsum dolor sit amet, consectetur adipiscing elit. Vestibulum pretium vel nibh id pulvinar. Morbi blandit mattis erat ut finibus.</p>

    <div class="brand">Velvet Crest</div>
    <div class="emblem" role="img" aria-label="Silver brand emblem area"></div>
    <div class="count">30<small>PILLS</small></div>
    <div class="tagline">male sexual performance pill</div>

    <div class="facts">
      <h2>Supplement Facts</h2>
      <div><strong>Serving Size: 2 Capsules</strong></div>
      <div><strong>Servings Per Container: 30</strong></div>
      <div class="rule-thick"></div>
      <div class="row"><span>Amount Per Serving</span><span>% Daily Value</span></div>
      <div class="rule-thin"></div>
      <div class="row"><span>VCX-Rx™ Proprietary Formula</span><span>1,550 mg †</span></div>
      <p>Horny Goat Weed (herb powder), Maca (herb powder), Mucuna Pruriens (L-Dopa), Polypodium Vulgare (herb powder), Yohimbe Bark (herb powder), Saw Palmetto (herb powder), Muira Puama (herb powder), Arginine (L-Arginine hydrochloride), Panax Ginseng (herb powder)</p>
      <div class="rule-thick"></div>
      <div><strong>† % Daily Value not established</strong></div>
      <div class="rule-thin"></div>
      <p><strong>Other Ingredients:</strong> Gelatin, Magnesium Stearate, and Calcium Carbonate.</p>
    </div>
    <p class="info"><strong>INFORMATION:</strong> Lorem ipsum dolor sit amet, consectetur adipiscing elit. Vestibulum pretium vel nibh id pulvinar. Morbi blandit mattis erat ut finibus. Morbi ornare lobortis nisl quis</p>

    <div class="web web--left">WWW.VELVETCRESTPILL.COM</div>
    <div class="web web--right">WWW.VELVETCRESTPILL.COM</div>
  </section>
</main>
</body>
</html>
```